Lumen+ Parlour Product Package Designs

We are currently launching a new spa, beauty and cosmetic product line called Lumen+ Parlour.

Our products ranging from pumice stones, sponges, and bath straps to cosmetic products.

There are four packaging label/product tags (please see attached templates as well as samples)

It needs to include:
Barcode placeholder
Product name placeholder
Area for brief product description (2-4 sentences)
website www.lumenplusparlour.example

Target Market(s)

end consumers (85% female)

Industry/Entity Type

Boutique

Font styles to use
Sans Serif
Decorative
Script

Colors
ffffff
e34197
e667a6
eda3c7
f9d9e8
fbd4d5
b768aa
d2a4cc

Requirements
Must have
• - Logo should be pink (do not modify the colour - shade can change slightly)
• - All four packaging designs should be combined into a single submission

```html
<!DOCTYPE html>
<html lang="en">
<head>
<meta charset="utf-8">
<title>Lumen+ Parlour – Bath Sponge Packaging</title>
<link rel="stylesheet" href="https://fonts.googleapis.com/css2?family=Alice&family=Tinos:ital,wght@0,400;0,700;1,400&display=swap">
<style>
  :root {
    --canvas-bg: #ececec;
    --white: #ffffff;
    --logo-pink: #e34197;
    --rose-deep: #b4485f;
    --rose-mid: #d9708a;
    --rose-text: #a8304c;
    --fuchsia-band: #e667a6;
    --fuchsia-tab: #e85aa8;
    --fuchsia-light: #f3a9cf;
    --fuchsia-deep: #e3168b;
    --fuchsia-text: #b0234f;
    --placeholder-fill: #f6f6f6;
    --placeholder-line: #9a9a9a;
  }
  * { box-sizing: border-box; margin: 0; padding: 0; }
  html, body { width: 907px; height: 1200px; overflow: hidden; }
  body { background: var(--canvas-bg); position: relative; font-family: "Tinos", serif; }

  .package {
    position: absolute; left: 55px; width: 797px; height: 557px;
    background: var(--white);
    box-shadow: 0 1px 4px rgba(0,0,0,0.08);
  }
  .package--rose { top: 30px; --accent: var(--rose-deep); --band: var(--rose-deep); --tab: var(--rose-deep); --ink: var(--rose-text);
    --art: linear-gradient(180deg, var(--rose-mid) 0%, #e69ab6 35%, var(--rose-deep) 70%, #e28fae 100%); }
  .package--fuchsia { top: 614px; --accent: var(--fuchsia-band); --band: var(--fuchsia-band); --tab: var(--fuchsia-tab); --ink: var(--fuchsia-text);
    --art: linear-gradient(180deg, #ec74b3 0%, var(--fuchsia-light) 35%, var(--fuchsia-deep) 72%, #f095c4 100%); }

  .hang-tab {
    position: absolute; top: 42px; width: 75px; height: 18px;
    background: var(--tab); border-radius: 9px;
  }
  .hang-tab::before {
    content: ""; position: absolute; left: 30px; top: -7px; width: 15px; height: 12px;
    background: var(--tab); border-radius: 8px 8px 0 0;
  }
  .hang-tab--left { left: 162px; }
  .hang-tab--right { left: 566px; }

  .leaf-artwork {
    position: absolute; left: 0; top: 108px; width: 797px; height: 449px;
    background: var(--art);
  }

  .front-label {
    position: absolute; left: 77px; top: 175px; width: 246px; height: 315px;
    background: var(--white);
  }
  .front-label__frame {
    position: absolute; inset: 10px; border: 2.5px solid var(--accent);
  }
  .brand-mark {
    position: absolute; left: 0; right: 0; top: 88px; text-align: center;
    font-family: "Alice", serif; font-size: 25px; color: var(--logo-pink);
  }
  .brand-mark__dot {
    display: block; width: 12px; height: 12px; margin: 0 auto 8px;
    border-radius: 50%; background: var(--logo-pink);
  }
  .product-band {
    position: absolute; left: 10px; right: 10px; top: 218px; height: 62px;
    background: var(--band); color: var(--white); text-align: center;
  }
  .product-band__name { font-family: "Alice", serif; font-size: 22px; margin-top: 8px; }
  .product-band__variant { font-style: italic; font-size: 12.5px; margin-top: 3px; }
  .net-weight {
    position: absolute; left: 0; right: 0; top: 285px; text-align: center;
    font-size: 10.5px; color: var(--ink);
  }

  .back-label {
    position: absolute; left: 460px; top: 148px; width: 287px; height: 369px;
    background: var(--white);
  }
  .back-label__frame {
    position: absolute; inset: 11px; border: 3px solid var(--accent);
    text-align: center; color: var(--ink); padding-top: 16px;
  }
  .back-label__intro { font-family: "Alice", serif; font-size: 16.5px; line-height: 22px; }
  .info-block { margin-top: 18px; font-size: 12.5px; line-height: 16px; }
  .info-block + .info-block { margin-top: 15px; }
  .info-block__title { font-size: 13px; }
  .info-block__line { opacity: 0.9; }
  .barcode-space {
    display: block; width: 98px; height: 46px; margin: 15px auto 0;
    background: var(--placeholder-fill); border: 1px solid var(--placeholder-line);
  }
  .legal { font-size: 11.5px; line-height: 14.5px; margin-top: 19px; padding: 0 14px; }
  .legal strong { font-weight: normal; }
  .website { font-size: 12px; font-weight: bold; margin-top: 8px; }
</style>
</head>
<body>

<section class="package package--rose" aria-label="Bath sponge package, rose edition">
  <div class="hang-tab hang-tab--left"></div>
  <div class="hang-tab hang-tab--right"></div>
  <div class="leaf-artwork" role="img" aria-label="Pattern of large rose-pink tropical monstera leaves"></div>

  <div class="front-label">
    <div class="front-label__frame"></div>
    <div class="brand-mark"><span class="brand-mark__dot"></span>Lumen+ Parlour</div>
    <div class="product-band">
      <p class="product-band__name">Bath Sponge</p>
      <p class="product-band__variant">Product description/variant</p>
    </div>
    <p class="net-weight">Netto 50g</p>
  </div>

  <div class="back-label">
    <div class="back-label__frame">
      <p class="back-label__intro">Describtions about the product<br>write here on short sentences.</p>
      <div class="info-block">
        <p class="info-block__title">Ingredients/Materials:</p>
        <p class="info-block__line">write down here</p>
        <p class="info-block__line">write down here</p>
      </div>
      <div class="info-block">
        <p class="info-block__title">Instructions/How to use:</p>
        <p class="info-block__line">write down here</p>
        <p class="info-block__line">write down here</p>
      </div>
      <div class="barcode-space" role="img" aria-label="Barcode placeholder"></div>
      <p class="legal">Manufactured in China<br>Distributed by <strong>Lumen Plus Parlour</strong> (Halden Bay, Canada)</p>
      <p class="website">www.lumenplusparlour.example</p>
    </div>
  </div>
</section>

<section class="package package--fuchsia" aria-label="Bath sponge package, fuchsia edition">
  <div class="hang-tab hang-tab--left"></div>
  <div class="hang-tab hang-tab--right"></div>
  <div class="leaf-artwork" role="img" aria-label="Pattern of large fuchsia watercolour monstera leaves"></div>

  <div class="front-label">
    <div class="front-label__frame"></div>
    <div class="brand-mark"><span class="brand-mark__dot"></span>Lumen+ Parlour</div>
    <div class="product-band">
      <p class="product-band__name">Bath Sponge</p>
      <p class="product-band__variant">Product description/variant</p>
    </div>
    <p class="net-weight">Netto 50g</p>
  </div>

  <div class="back-label">
    <div class="back-label__frame">
      <p class="back-label__intro">Describtions about the product<br>write here on short sentences.</p>
      <div class="info-block">
        <p class="info-block__title">Ingredients/Materials:</p>
        <p class="info-block__line">write down here</p>
        <p class="info-block__line">write down here</p>
      </div>
      <div class="info-block">
        <p class="info-block__title">Instructions/How to use:</p>
        <p class="info-block__line">write down here</p>
        <p class="info-block__line">write down here</p>
      </div>
      <div class="barcode-space" role="img" aria-label="Barcode placeholder"></div>
      <p class="legal">Manufactured in China<br>Distributed by <strong>Lumen Plus Parlour</strong> (Halden Bay, Canada)</p>
      <p class="website">www.lumenplusparlour.example</p>
    </div>
  </div>
</section>

</body>
</html>
```